Brightvale Capital brochure for Investment partnership, young harold pemby

We need a brochure design to attract new investors for our investing partnership Called Brighttvale Capital. We are based in New Orleans, La. We primarily invest in stocks, bonds, and crypto but venture out into other categories as well. We would like to see designs with the black and gold like our logo. The final design should say new, fresh, sleek, tech, and honorable. BROUCHURE WILL BE 4 pages.or one folded sheet a paparer if that makes sense.

A chart showing Brighttvae Capital gains since 2019 28.6 percent and the KT 300 gAINS 7.1 PERCENT

Probable Investors

Financial Planning

• Black and Gold accent. Stock market feel. Sleek, High tech, innovative, Intellgent design.
• Page colors possibly black.
• Boring, Old school,

```html
<!DOCTYPE html>
<html lang="en">
<head>
<meta charset="utf-8">
<title>Brightvale Capital – Brochure</title>
<link rel="stylesheet" href="https://fonts.googleapis.com/css2?family=Montserrat:wght@400;500&family=Tinos:ital,wght@0,400;0,700;1,700&display=swap">
<style>
  :root {
    --canvas: #e8e8e8;
    --ink-black: #0b0b0b;
    --ink-charcoal: #272727;
    --gold: #d4a72c;
    --gold-line: #c99b22;
    --paper-text: #f2f2f2;
    --muted-text: #d8d8d8;
    --serif: "Tinos", "Times New Roman", serif;
    --sans: "Montserrat", Arial, sans-serif;
  }
  * { box-sizing: border-box; margin: 0; padding: 0; }
  html, body { width: 848px; height: 1200px; overflow: hidden; }
  body { background: var(--canvas); position: relative; font-family: var(--sans); }

  .spread { position: absolute; left: 34px; width: 780px; height: 500px; overflow: hidden;
            box-shadow: 0 10px 28px rgba(0,0,0,.22); }
  .spread--outer { top: 50px; background: var(--ink-black); }
  .spread--inner { top: 640px; background: var(--ink-charcoal); }
  .spread svg.shapes { position: absolute; inset: 0; }

  .about-title { position: absolute; left: 50px; top: 104px; width: 320px; text-align: center;
                 font: italic 700 20px/1.15 var(--serif); color: var(--gold); }
  .about-body { position: absolute; left: 52px; top: 170px; width: 245px;
                font: 400 10.5px/1.55 var(--sans); color: var(--muted-text); text-align: justify; }

  .brand-name { position: absolute; left: 628px; top: 112px; width: 140px; text-align: center;
                font: 400 22px/1 var(--serif); color: var(--gold); letter-spacing: .5px; }
  .brand-name span { display: block; font-size: 11px; letter-spacing: 5px; margin-top: 4px; }

  .tagline { position: absolute; left: 300px; top: 394px; width: 450px; text-align: center;
             font: 400 15px/1.35 var(--serif); color: #fff; }
  .tagline em { display: block; font-style: italic; font-weight: 700; }

  .invite-text { position: absolute; left: 100px; top: 44px; width: 210px;
                 font: 400 10px/1.6 var(--sans); color: var(--muted-text); }
  .invite-text strong { display: block; margin-top: 6px; text-align: right;
                        font: italic 700 13px/1 var(--serif); color: #fff; }

  .gains-title { position: absolute; left: 40px; top: 238px; font: italic 700 21px/1 var(--serif); color: var(--gold); }

  .how-title { position: absolute; left: 425px; top: 60px; font: italic 700 18px/1 var(--serif); color: var(--gold); }
  .steps { position: absolute; left: 425px; top: 100px; width: 325px; list-style: none; counter-reset: step; }
  .steps li { position: relative; padding-left: 24px; margin-bottom: 16px;
              font: 400 10.5px/1.65 var(--sans); color: var(--muted-text); counter-increment: step; }
  .steps li::before { content: counter(step); position: absolute; left: 0; top: 0; color: var(--paper-text); }
</style>
</head>
<body>

<!-- Outer spread: back page + cover -->
<section class="spread spread--outer">
  <svg class="shapes" width="780" height="500" viewBox="0 0 780 500">
    <defs>
      <linearGradient id="streetTone" x1="0" y1="0" x2="1" y2="1">
        <stop offset="0" stop-color="#5a5a5a"/>
        <stop offset=".45" stop-color="#8d8d8d"/>
        <stop offset=".7" stop-color="#3c3c3c"/>
        <stop offset="1" stop-color="#151515"/>
      </linearGradient>
    </defs>
    <polygon role="img" aria-label="Black and white photograph of a historic cathedral with an iron fence and balconied street"
             points="300,0 560,0 690,300 610,360 300,390 120,500 0,500 0,470 250,330 420,220" fill="url(#streetTone)"/>
    <polygon points="408,205 440,245 290,322 312,296 402,246" fill="var(--gold)"/>
    <polyline points="585,40 715,300 620,360" fill="none" stroke="var(--gold-line)" stroke-width="1.5"/>
    <polygon points="330,385 770,385 720,470 280,470" fill="var(--gold)"/>
  </svg>

  <h2 class="about-title">About Bright vale Capital<br>and General Partner</h2>
  <p class="about-body">Brightvale Capital was founded in 2019 by General Partner Desmond Whitaker Jr with a group economic empowerment mission. Desmond Whitaker has invested int stocks since a teenager received his BA in ecomics from Eastbrook State University and is currently attending The University of Harlow Bay.</p>

  <div class="brand-name">Brightvale<span>Capital</span></div>

  <p class="tagline">Become a partner and build generational<br>wealth by investing in the stock market<em>“ A first of its kind Investment Club ”</em></p>
</section>

<!-- Inner spread -->
<section class="spread spread--inner">
  <svg class="shapes" width="780" height="500" viewBox="0 0 780 500">
    <defs>
      <linearGradient id="cityTone" x1="0" y1="0" x2="1" y2="0">
        <stop offset="0" stop-color="#1e1e1e"/>
        <stop offset=".5" stop-color="#2c2c2c"/>
        <stop offset="1" stop-color="#3a3a3a"/>
      </linearGradient>
    </defs>
    <rect role="img" aria-label="Faint dark photograph of a city street with storefronts and palm trees"
          width="780" height="500" fill="url(#cityTone)"/>
    <polygon points="60,25 290,25 340,220 110,220" fill="none" stroke="var(--gold-line)" stroke-width="1"/>

    <g class="chart" font-family="Montserrat, Arial, sans-serif" font-size="8" fill="#cfcfcf">
      <text x="40" y="296">Since 2019</text>
      <text x="40" y="318">KT 300</text>
      <text x="40" y="346">Brightvale</text>
      <rect x="100" y="306" width="62" height="18" fill="var(--gold)"/>
      <rect x="100" y="334" width="248" height="18" fill="var(--gold)"/>
      <text x="168" y="319">7.1 %</text>
      <text x="300" y="366" fill="var(--paper-text)">28.6 %</text>
      <g fill="var(--gold)">
        <text x="97" y="380">0</text><text x="139" y="380">5</text><text x="180" y="380">10</text>
        <text x="223" y="380">15</text><text x="266" y="380">20</text><text x="310" y="380">25</text>
        <text x="353" y="380">30</text>
      </g>
    </g>

    <polygon points="0,425 390,468 390,478 0,436" fill="var(--gold)"/>
    <rect x="390" y="472" width="390" height="6" fill="var(--gold)"/>
  </svg>

  <p class="invite-text">If you are receiving this brochure its because someone sees you as a person that doesn't want to just work and pay bills. Your someone who wants to build real generational wealth. Not throw schemes but the using the greatest wealth builder available:<strong>The Stock Market.</strong></p>

  <h2 class="gains-title">Capital Gains</h2>

  <h2 class="how-title">How it works</h2>
  <ol class="steps">
    <li>Make initial deposit. The general partner will invest in stocks, bonds and other investment vehicles on your behalf.</li>
    <li>There is no upfront fees. The general partner will guarantee a 5 percent return and will work for free on your behalf until that is achieved. After the 5 percent return on the dollars invested the limited partner will receive 80 percent and the general partner will receive 20 percent of every dollar gained.</li>
    <li>As the return and investments multiply the interests begins to compound annually. The legal partner legally owns shares of stock within the club and may redeem once a year or let money continue to earn interest.</li>
  </ol>
</section>

</body>
</html>
```